REDESIGN SIGN UP PAGE - EASY TO READ AND UNDERSTAND QUICKLY

I need to redesign my sign up page DESKTOP AND MOBILE VERSION to include 2 products that are each available as a monthly subscription, 6 mth or 12 mth subscription.

Currently I only promote one product on my website but now will be two. https://www.brightlanerewardhub.biz/signup

Now I will have two products:

1. UNLIMITED VACATION CERTIFICATES, DINING VOUCHERS & SAVINGS INCENTIVES
Unlimited Monthly Plan $99 / Month + $199 One-Time Set-Up Fee
Unlimited Bi Annual Plan $490 / 6 Months + $199 One-Time Set-Up Fee
Unlimited Annual Plan $898 / 12 Months + $199 One-Time Set-Up Fee

2. UNLIMITED SMART DEVICE INCENTIVES & OTHER HARD PREMIUMS
Unlimited Monthly Plan $299 / Month + $199 One-Time Set-Up Fee
Unlimited Bi Annual Plan $1,590 / 6 Months + $199 One-Time Set-Up Fee
Unlimited Annual Plan $2,898 / 12 Months + $199 One-Time Set-Up Fee

When promoting the different plans you can see the different categories of incentives I offer here: https://www.brightlanerewardhub.biz/incentives

The SMART DEVICE CERTIFICATES & INCENTIVES category is for product #2 and all the rest of the Categories is for Product #1 Feel free to use images as a visual so customers can see that this product includes Vacations & Restaurants and this product includes only smart devices....

USE ALL CURRENT BULLET POINTS FOR BOTH PLANS THAT IS CURRENTLY ON WEBSITE. USE ALL CURRENT CONTENT ON WEBSITE ORIGINAL SIGN UP PAGE. DO NOT LEAVE ANY CONTENT OUT.

Target Market(s)

BUSINESS OWNERS

Industry/Entity Type

Marketing

Number of Pages Required

2 page

Requirements
Must have
• When promoting the 2 different products on the new sign up page you can see the different categories of incentives I offer here: https://www.brightlanerewardhub.biz/incentives fee; free to use images to showcase what each product offers.

The SMART DEVICE CERTIFICATES & INCENTIVES category is for product #2 and all the rest of the Categories is for Product #1

I want the user to easily understand we have two products that are available in 3 ways, monthly subscription, bi annual and annual and can see the price immediately for all 3 options for both products without toggling, etc.

Must be super clean easy to ready design. Not too busy at all please
Nice to have
• USE ALL CURRENT BULLET POINTS FOR BOTH PLANS THAT IS CURRENTLY ON WEBSITE. USE ALL CURRENT CONTENT ON WEBSITE ORIGINAL SIGN UP PAGE. DO NOT LEAVE ANY CONTENT OUT.

Should not have

```html
<!DOCTYPE html>
<html lang="en">
<head>
<meta charset="utf-8">
<title>Sign Up – Brightlane Reward Hub</title>
<link href="https://fonts.googleapis.com/css2?family=Montserrat:wght@400;500;600;700&display=swap" rel="stylesheet">
<style>
:root{
  --blue:#1a75bb;
  --green:#4caf50;
  --ink:#111;
  --text:#555;
  --muted:#8a8a8a;
  --tint:#eaf4fb;
  --white:#fff;
  --footer:#1c1d1f;
  --footer-text:#b9bcc0;
  --bottom:#0d0d0d;
}
*{margin:0;padding:0;box-sizing:border-box}
html,body{width:1200px;height:4283px;overflow:hidden}
body{font-family:"Montserrat",sans-serif;color:var(--ink);background:var(--white);position:relative}
a{color:inherit;text-decoration:none}

.site-header{position:absolute;top:0;left:0;width:1200px;height:93px;background:var(--tint)}
.brand{position:absolute;left:90px;top:34px;font-weight:700;font-size:22px;color:var(--blue);display:flex;align-items:center;gap:8px}
.brand-dot{width:14px;height:14px;background:var(--blue);border-radius:50%}
.main-nav{position:absolute;left:0;top:44px;width:950px;height:20px;font-size:12px;font-weight:500;white-space:nowrap}
.main-nav a{position:absolute;top:0}
.main-nav .active{color:var(--blue)}
.main-nav .active::after{content:"";position:absolute;left:-4px;right:-4px;top:46px;height:3px;background:var(--blue)}
.btn-signup{position:absolute;left:957px;top:35px;width:83px;height:31px;background:var(--blue);color:#fff;font-size:12px;font-weight:600;display:flex;align-items:center;justify-content:center;border-radius:2px}
.btn-login{position:absolute;left:1059px;top:43px;font-size:12px;font-weight:600}

.intro{position:absolute;top:183px;left:0;width:1200px;text-align:center;font-size:23px;line-height:39px}
.section-title{position:absolute;left:0;width:1200px;text-align:center;font-weight:700;font-size:35px;line-height:45px}
.section-title span{display:block;color:var(--blue)}
.bar{position:absolute;left:580px;width:40px;height:6px;border-radius:3px;background:var(--blue)}

.plan-card{position:absolute;width:313px;height:435px;background:#fff;border-radius:22px;box-shadow:0 8px 30px rgba(0,0,0,.08);text-align:center}
.plan-name{margin-top:58px;font-size:22px;font-weight:700;line-height:34px}
.plan-price{margin-top:8px;font-size:38px;font-weight:700;line-height:46px}
.plan-price sup{font-size:16px;font-weight:500;vertical-align:22px;margin-right:4px}
.plan-term{margin-top:12px;font-size:14px;color:var(--blue)}
.plan-term b{font-weight:700}
.plan-fee{margin-top:8px;font-size:12px;color:var(--green)}
.plan-desc{margin:34px auto 0;width:230px;font-size:13.5px;line-height:23px;color:var(--muted)}
.plan-select{position:absolute;left:71px;bottom:-27px;width:170px;height:50px;border-radius:12px;background:#fff;border:2px solid var(--blue);font-size:18px;font-weight:700;display:flex;align-items:center;justify-content:center}
.plan-card.featured-blue{background:var(--blue);color:#fff}
.plan-card.featured-green{background:var(--green);color:#fff}
.plan-card.featured-blue .plan-term,.plan-card.featured-blue .plan-fee,.plan-card.featured-blue .plan-desc,
.plan-card.featured-green .plan-term,.plan-card.featured-green .plan-fee,.plan-card.featured-green .plan-desc{color:#fff}
.featured-blue .plan-select{background:var(--green);border-color:var(--green);color:#fff}
.featured-green .plan-select{background:var(--blue);border-color:var(--blue);color:#fff}

.compare{position:absolute;top:1800px;left:0;width:1200px;height:1660px;background:var(--tint)}
.compare-title{position:absolute;top:75px;left:0;width:1200px;text-align:center;font-size:36px;font-weight:500}
.compare-lead{position:absolute;top:180px;left:290px;width:620px;text-align:center;font-size:16px;line-height:25px;color:var(--text)}
.plan-head{position:absolute;top:282px;left:83px;width:1029px;height:97px;background:#fff;border-radius:18px}
.plan-head h2{position:absolute;left:58px;top:26px;font-size:36px;font-weight:600}
.plan-head .col{position:absolute;top:38px;width:200px;margin-left:-100px;text-align:center;font-size:17px;font-weight:600}
.features{position:absolute;top:403px;left:138px;width:940px;list-style:none}
.features li{position:relative;display:flex;align-items:center;min-height:54px;font-size:16.5px;color:var(--text)}
.features li.two{min-height:81px}
.features .label{width:340px;line-height:27px}
.features .tick{position:absolute;left:0;width:30px;height:30px;margin-left:-15px}
.features .t1{left:485px}.features .t2{left:680px}.features .t3{left:877px}

.site-footer{position:absolute;top:3460px;left:0;width:1200px;height:756px;background:var(--footer)}
.footer-logo{position:absolute;top:75px;left:0;width:1200px;display:flex;justify-content:center;align-items:center;gap:8px;font-size:22px;font-weight:700;color:var(--blue)}
.social{position:absolute;top:130px;left:512px;display:flex;gap:28px}
.social span{width:20px;height:20px;border-radius:50%;background:#fff}
.btn-samples{position:absolute;top:185px;left:437px;width:336px;height:71px;background:var(--green);color:#fff;font-size:18px;font-weight:700;display:flex;align-items:center;justify-content:center;border-radius:2px}
.f-col{position:absolute;top:328px}
.f-col h3{font-size:19px;font-weight:600;color:#fff;margin-bottom:18px}
.f-links{list-style:none;font-size:14.5px;line-height:33.7px;color:var(--footer-text);white-space:nowrap}
.f-links .on{color:#fff}
.contact{list-style:none;font-size:14.5px;line-height:27px;color:var(--footer-text)}
.contact li{position:relative;padding-left:36px;margin-bottom:18px}
.contact svg{position:absolute;left:0;top:4px}
.contact b{color:#fff;font-weight:600}
.contact .closed{color:var(--green)}
.bottom-bar{position:absolute;top:4216px;left:0;width:1200px;height:67px;background:var(--bottom);color:#fff;font-size:14.5px}
.bottom-bar .copy{position:absolute;left:83px;top:23px}
.bottom-bar .legal{position:absolute;right:93px;top:23px}
</style>
</head>
<body>

<header class="site-header">
  <div class="brand"><span class="brand-dot"></span>Brightlane Reward Hub</div>
  <nav class="main-nav">
    <a class="active" href="#" style="left:521px">Home</a>
    <a href="https://www.brightlanerewardhub.biz/incentives" style="left:580px">The Incentives</a>
    <a href="#" style="left:692px">Samples</a>
    <a href="#" style="left:767px">Industries</a>
    <a href="#" style="left:850px">Integrations</a>
  </nav>
  <a class="btn-signup" href="https://www.brightlanerewardhub.biz/signup">Signup</a>
  <a class="btn-login" href="#">Login</a>
</header>

<p class="intro">This program is an online subscription based incentive<br>marketing system with the following features</p>

<h1 class="section-title" style="top:310px">Unlimited Vacation Certificates,<span>Dining Vouchers &amp; Savings Incentives</span></h1>
<div class="bar" style="top:432px"></div>

<article class="plan-card" style="left:86px;top:482px">
  <h3 class="plan-name">Unlimited<br>Monthly Plan</h3>
  <div class="plan-price"><sup>$</sup>99</div>
  <div class="plan-term">Month + <b>$199</b></div>
  <div class="plan-fee">One-Time Set-Up Fee</div>
  <p class="plan-desc">Lorem ipsum dolor sit amet, consectetur adipiscing elit, sed do eiusmod tempor incididunt ut labore et dolore magna</p>
  <a class="plan-select" href="#">Select</a>
</article>
<article class="plan-card featured-blue" style="left:444px;top:482px">
  <h3 class="plan-name">Unlimited<br>Monthly Plan</h3>
  <div class="plan-price"><sup>$</sup>490</div>
  <div class="plan-term">6 Month + <b>$199</b></div>
  <div class="plan-fee">One-Time Set-Up Fee</div>
  <p class="plan-desc">Lorem ipsum dolor sit amet, consectetur adipiscing elit, sed do eiusmod tempor incididunt ut labore et dolore magna</p>
  <a class="plan-select" href="#">Select</a>
</article>
<article class="plan-card" style="left:803px;top:482px">
  <h3 class="plan-name">Unlimited<br>Annual Plan</h3>
  <div class="plan-price"><sup>$</sup>898</div>
  <div class="plan-term">12 Month + <b>$199</b></div>
  <div class="plan-fee">One-Time Set-Up Fee</div>
  <p class="plan-desc">Lorem ipsum dolor sit amet, consectetur adipiscing elit, sed do eiusmod tempor incididunt ut labore et dolore magna</p>
  <a class="plan-select" href="#">Select</a>
</article>

<h2 class="section-title" style="top:1068px">Unlimited Smart Device<span>Incentives &amp; Other Hard Premiums</span></h2>
<div class="bar" style="top:1190px"></div>

<article class="plan-card" style="left:86px;top:1240px">
  <h3 class="plan-name">Unlimited<br>Monthly Plan</h3>
  <div class="plan-price"><sup>$</sup>299</div>
  <div class="plan-term">Month + <b>$199</b></div>
  <div class="plan-fee">One-Time Set-Up Fee</div>
  <p class="plan-desc">Lorem ipsum dolor sit amet, consectetur adipiscing elit, sed do eiusmod tempor incididunt ut labore et dolore magna</p>
  <a class="plan-select" href="#">Select</a>
</article>
<article class="plan-card featured-green" style="left:444px;top:1240px">
  <h3 class="plan-name">Unlimited<br>Monthly Plan</h3>
  <div class="plan-price"><sup>$</sup>1.590</div>
  <div class="plan-term">6 Month + <b>$199</b></div>
  <div class="plan-fee">One-Time Set-Up Fee</div>
  <p class="plan-desc">Lorem ipsum dolor sit amet, consectetur adipiscing elit, sed do eiusmod tempor incididunt ut labore et dolore magna</p>
  <a class="plan-select" href="#">Select</a>
</article>
<article class="plan-card" style="left:803px;top:1240px">
  <h3 class="plan-name">Unlimited<br>Annual Plan</h3>
  <div class="plan-price"><sup>$</sup>2.898</div>
  <div class="plan-term">12 Month + <b>$199</b></div>
  <div class="plan-fee">One-Time Set-Up Fee</div>
  <p class="plan-desc">Lorem ipsum dolor sit amet, consectetur adipiscing elit, sed do eiusmod tempor incididunt ut labore et dolore magna</p>
  <a class="plan-select" href="#">Select</a>
</article>

<section class="compare">
  <h2 class="compare-title">Our Pricing is Fair</h2>
  <div class="bar" style="top:153px"></div>
  <p class="compare-lead">Lorem ipsum dolor sit amet, consectetur adipiscing elit, sed do eiusmod tempor incididunt ut labore et dolore magna aliqua. Quis ipsum</p>
  <div class="plan-head">
    <h2>Plan</h2>
    <div class="col" style="left:540px">Monthly Plan</div>
    <div class="col" style="left:735px">Monthly Plan</div>
    <div class="col" style="left:932px">Annual Plan</div>
  </div>
  <svg width="0" height="0" style="position:absolute">
    <symbol id="tick" viewBox="0 0 30 30"><path d="M3 15.5 11.5 24 27 7" fill="none" stroke="#4caf50" stroke-width="4.5" stroke-linecap="round" stroke-linejoin="round"/></symbol>
  </svg>
  <ul class="features">
    <li><span class="label">Unlimited E-certificates</span><svg class="tick t1"><use href="#tick"/></svg><svg class="tick t2"><use href="#tick"/></svg><svg class="tick t3"><use href="#tick"/></svg></li>
    <li><span class="label">Unlimited SMS Certificates</span><svg class="tick t1"><use href="#tick"/></svg><svg class="tick t2"><use href="#tick"/></svg><svg class="tick t3"><use href="#tick"/></svg></li>
    <li><span class="label">Unlimited Web Banner Certificates</span><svg class="tick t1"><use href="#tick"/></svg><svg class="tick t2"><use href="#tick"/></svg><svg class="tick t3"><use href="#tick"/></svg></li>
    <li class="two"><span class="label">Unlimited White Label Certificate<br>Landing Pages</span><svg class="tick t1"><use href="#tick"/></svg><svg class="tick t2"><use href="#tick"/></svg><svg class="tick t3"><use href="#tick"/></svg></li>
    <li><span class="label">Unlimited Website POPup Certificate</span><svg class="tick t1"><use href="#tick"/></svg><svg class="tick t2"><use href="#tick"/></svg><svg class="tick t3"><use href="#tick"/></svg></li>
    <li><span class="label">Unlimited API E-Certificates</span><svg class="tick t1"><use href="#tick"/></svg><svg class="tick t2"><use href="#tick"/></svg><svg class="tick t3"><use href="#tick"/></svg></li>
    <li><span class="label">Unlimited Automation Intergatioin Access</span><svg class="tick t1"><use href="#tick"/></svg><svg class="tick t2"><use href="#tick"/></svg><svg class="tick t3"><use href="#tick"/></svg></li>
    <li><span class="label">Free warm Lead Letter Templates</span><svg class="tick t1"><use href="#tick"/></svg><svg class="tick t2"><use href="#tick"/></svg><svg class="tick t3"><use href="#tick"/></svg></li>
    <li><span class="label">Free Warm LEAD Letter Templates</span><svg class="tick t1"><use href="#tick"/></svg><svg class="tick t2"><use href="#tick"/></svg><svg class="tick t3"><use href="#tick"/></svg></li>
    <li class="two"><span class="label">Free Costomer Appreciation Letter<br>Templates</span><svg class="tick t1"><use href="#tick"/></svg><svg class="tick t2"><use href="#tick"/></svg><svg class="tick t3"><use href="#tick"/></svg></li>
    <li class="two"><span class="label">Free Professional _ Grade Incentive<br>Videos</span><svg class="tick t1"><use href="#tick"/></svg><svg class="tick t2"><use href="#tick"/></svg><svg class="tick t3"><use href="#tick"/></svg></li>
    <li><span class="label">FREE Proven Social Media Ad Templates</span><svg class="tick t1"><use href="#tick"/></svg><svg class="tick t2"><use href="#tick"/></svg><svg class="tick t3"><use href="#tick"/></svg></li>
    <li class="two"><span class="label">FREE High-Converting Banner Ad<br>Templates</span><svg class="tick t1"><use href="#tick"/></svg><svg class="tick t2"><use href="#tick"/></svg><svg class="tick t3"><use href="#tick"/></svg></li>
    <li><span class="label">FREE Time-Tested Print Ad Templates</span><svg class="tick t1"><use href="#tick"/></svg><svg class="tick t2"><use href="#tick"/></svg><svg class="tick t3"><use href="#tick"/></svg></li>
    <li><span class="label">FREE White Label Redemption Website</span><svg class="tick t1"><use href="#tick"/></svg><svg class="tick t2"><use href="#tick"/></svg><svg class="tick t3"><use href="#tick"/></svg></li>
    <li><span class="label">FREE Industry Specific Ad Packs</span><svg class="tick t1"><use href="#tick"/></svg><svg class="tick t2"><use href="#tick"/></svg><svg class="tick t3"><use href="#tick"/></svg></li>
    <li class="two"><span class="label">FREE Affiliate Program-Earn 50%<br>Commissions</span><svg class="tick t1"><use href="#tick"/></svg><svg class="tick t2"><use href="#tick"/></svg><svg class="tick t3"><use href="#tick"/></svg></li>
    <li class="two"><span class="label">FREE Eye-Catching Posters, Flyers &amp;<br>Brochures Each Certificate</span><svg class="tick t1"><use href="#tick"/></svg><svg class="tick t2"><use href="#tick"/></svg><svg class="tick t3"><use href="#tick"/></svg></li>
    <li><span class="label">FREE Step by Step Redemption Guides</span><svg class="tick t1"><use href="#tick"/></svg><svg class="tick t2"><use href="#tick"/></svg><svg class="tick t3"><use href="#tick"/></svg></li>
  </ul>
</section>

<footer class="site-footer" role="img" aria-label="Dark photographic backdrop of a business desk behind the footer">
  <div class="footer-logo"><span class="brand-dot"></span>Brightlane Reward Hub</div>
  <div class="social" aria-label="Social links"><span></span><span></span><span></span><span></span></div>
  <a class="btn-samples" href="#">Get Free Samples 100% free</a>

  <div class="f-col" style="left:83px;width:380px">
    <h3>CONTACT US</h3>
    <ul class="contact">
      <li><svg width="16" height="20" viewBox="0 0 16 20"><path d="M8 0a7 7 0 0 0-7 7c0 5 7 13 7 13s7-8 7-13a7 7 0 0 0-7-7zm0 10a3 3 0 1 1 0-6 3 3 0 0 1 0 6z" fill="#fff"/></svg>Brightlane Reward Hub Group, Inc.<br>4470 Harbor Crest Avenue Suite 310<br>Fairview, CA 90210</li>
      <li><svg width="18" height="18" viewBox="0 0 18 18"><path d="M4 1l3 4-2 2c1 2 3 4 5 5l2-2 4 3-2 3C8 16 2 10 1 4z" fill="#fff"/></svg><b>USA Office:</b> 1-555-214-7730<br><b>International:</b> 1-800-555-0148<br><b>Text Us:</b> 1-555-302-6615</li>
      <li><svg width="18" height="18" viewBox="0 0 18 18"><circle cx="9" cy="9" r="8" fill="none" stroke="#fff" stroke-width="1.6"/><path d="M1 9h16M9 1c3 3 3 13 0 16M9 1c-3 3-3 13 0 16" fill="none" stroke="#fff" stroke-width="1.4"/></svg>info@brightlanerewardhub.biz</li>
      <li><svg width="18" height="18" viewBox="0 0 18 18"><circle cx="9" cy="9" r="9" fill="#fff"/><path d="M9 4v5l3 2" fill="none" stroke="#1c1d1f" stroke-width="1.8"/></svg><b>Monday - Friday</b> &nbsp;8am - 5pm PST<br><span class="closed">Sat/Sun/Holidays Closed</span></li>
    </ul>
  </div>

  <div class="f-col" style="left:542px">
    <h3>QUICK LINKS</h3>
    <ul class="f-links">
      <li>Home</li><li class="on">The Incentives</li><li>Samples</li><li>Affiliate</li><li>Testimonials</li><li>Faq</li><li>Contact Us</li><li>Redemption Demo Videos</li><li>Brightlane Distribute Certificate</li><li>Demo Videos</li>
    </ul>
  </div>

  <div class="f-col" style="left:876px">
    <h3>QUICK LINKS</h3>
    <ul class="f-links">
      <li>Hoteliers</li><li>Brightlane Certificates List</li><li>How To Use Brightlane Certificates</li><li>Social Incentive Campaign</li><li>Pop Ups &amp; Sticky Bars</li><li>Whitepaper - Increase Sales</li><li>Whitepaper - Improve Sales</li><li>During Strange Times</li><li>Whitepaper - Boost Website</li><li>Conversions</li>
    </ul>
  </div>
</footer>

<div class="bottom-bar">
  <span class="copy">© 2020 Brightlane Reward Hub Group, Inc. All Rights Reserved.</span>
  <span class="legal">Privacy Policy &nbsp;|&nbsp; Term And Conditions</span>
</div>

</body>
</html>
```